Non Profit raising scholarship funds needs flyer for Golf Tournament

We need a flyer for our upcoming golf tournament. Proceeds to will help to benefit our Pathway builders learning grant fund.

Title: 2019 O-RamVT Golf Tournament
Location: Brindle Oaks Links
Date: May 15, 2019
Registration: $175 individual, $700 foursome
Sponsorships starting at $250
Benefiting O-RamVT and the Pathway Builders Learning Grant Fund

Target Market(s)

Design and Construction industry professionals

Industry/Entity Type

Construction

Font styles to use
Serif
Sans Serif

Colors

Designer to choose colors to be used in the design.

Requirements
Must have
• Title, date, location, registration info, sponsor info, benefit info, logo
Nice to have
• I like the retro look of some golf flyers, but it's not necessary
Should not have
• .

```html
<!DOCTYPE html>
<html lang="en">
<head>
<meta charset="utf-8">
<title>2019 O-RamVT Golf Tournament</title>
<link rel="stylesheet" href="https://fonts.googleapis.com/css2?family=Archivo+Black&family=Oswald:wght@600&family=Roboto+Slab:wght@500&family=Signika:wght@400;500&display=swap">
<style>
  :root {
    --green-deep: #14260f;
    --green-mid: #4f9a2e;
    --green-light: #a9d77a;
    --green-pale: #dcefc6;
    --line-green: #8dbb4a;
    --text-green: #5f8f2e;
    --orange: #e07b3a;
    --white: #ffffff;
    --grey-edge: #8a8f8a;
    --navy: #2f4a9a;
    --ink-green: #25461a;
  }
  * { margin: 0; padding: 0; box-sizing: border-box; }
  html, body { width: 848px; height: 1200px; overflow: hidden; background: var(--white); }
  .flyer {
    position: relative; width: 848px; height: 1200px; overflow: hidden;
    background: linear-gradient(180deg, var(--green-deep) 0%, #2f6a1f 28%, var(--green-mid) 48%, var(--green-light) 68%, var(--green-pale) 100%);
    font-family: "Signika", sans-serif;
  }
  .hero-photo {
    position: absolute; left: 120px; top: 220px; width: 600px; height: 640px;
    background: radial-gradient(ellipse 46% 42% at 50% 44%, rgba(180,200,215,0.85) 0%, rgba(150,180,190,0.55) 55%, rgba(120,170,120,0) 100%);
    filter: blur(6px);
  }
  .lower-panel {
    position: absolute; left: 0; top: 896px; width: 848px; height: 304px;
    background: linear-gradient(180deg, rgba(235,246,220,0.55), rgba(245,250,238,0.8));
  }
  .logo-badge {
    position: absolute; left: 318px; top: 28px; width: 208px; height: 208px;
    border-radius: 50%; background: var(--white);
    display: flex; align-items: center; justify-content: center;
  }
  .logo-name { font-family: "Signika", sans-serif; font-weight: 500; font-size: 44px; color: var(--navy); }
  .event-org {
    position: absolute; top: 282px; width: 100%; text-align: center;
    font-family: "Roboto Slab", serif; font-weight: 500; font-size: 64px;
    letter-spacing: 18px; color: var(--white); padding-left: 18px;
  }
  .event-golf {
    position: absolute; top: 340px; width: 100%; text-align: center;
    font-family: "Archivo Black", sans-serif; font-size: 236px; line-height: 1;
    color: var(--white); -webkit-text-stroke: 4px var(--grey-edge); paint-order: stroke fill;
    letter-spacing: -6px; padding-left: 50px;
  }
  .event-tournament {
    position: absolute; top: 552px; width: 100%; text-align: center;
    font-family: "Oswald", sans-serif; font-weight: 600; font-size: 70px; line-height: 1;
    color: var(--white); letter-spacing: 2px;
  }
  .ribbon { position: absolute; left: 0; top: 560px; }
  .event-year {
    position: absolute; top: 664px; left: 112px; width: 630px; text-align: center;
    font-family: "Archivo Black", sans-serif; font-size: 82px; line-height: 1;
    letter-spacing: 64px; padding-left: 64px;
    background: linear-gradient(180deg, #0e1f0a, #4d7a2c);
    -webkit-background-clip: text; background-clip: text; color: transparent;
  }
  .connectors { position: absolute; left: 0; top: 880px; }
  .detail {
    position: absolute; left: 146px; font-size: 29px; color: var(--text-green); line-height: 1.3;
  }
  .detail-location { top: 946px; }
  .detail-price { top: 1016px; }
  .price { color: var(--orange); }
  .date-box {
    position: absolute; left: 408px; top: 944px; width: 404px; height: 146px;
    border: 3px solid var(--line-green); background: rgba(255,255,255,0.35);
    display: flex; align-items: center; justify-content: center;
    font-size: 60px; color: var(--text-green);
  }
  .date-day { color: var(--orange); margin: 0 2px 0 14px; }
  .divider { position: absolute; left: 150px; top: 1112px; width: 548px; height: 3px; background: var(--line-green); }
  .sponsor-line, .benefit-line {
    position: absolute; width: 100%; text-align: center;
    font-family: Arial, Helvetica, sans-serif; font-size: 19px; letter-spacing: 1px; color: var(--text-green);
  }
  .sponsor-line { top: 1128px; }
  .benefit-line { top: 1157px; }
</style>
</head>
<body>
<main class="flyer">
  <div class="hero-photo" role="img" aria-label="Blurred golf ball resting on a tee above the green"></div>
  <div class="lower-panel"></div>

  <div class="logo-badge"><span class="logo-name">O-RamVT</span></div>

  <h1>
    <span class="event-org">O-RamVT</span>
    <span class="event-golf">GOLF</span>
  </h1>

  <svg class="ribbon" width="848" height="260" viewBox="0 0 848 260" aria-hidden="true">
    <g fill="#ffffff">
      <polygon points="38,116 196,116 196,250 38,250 78,183"/>
      <polygon points="810,116 652,116 652,250 810,250 770,183"/>
      <polygon points="196,116 196,250 112,216" fill="#d9dcd6"/>
      <polygon points="652,116 652,250 742,216" fill="#d9dcd6"/>
      <rect x="112" y="82" width="630" height="134" style="filter:drop-shadow(0 6px 6px rgba(0,0,0,0.35))"/>
    </g>
    <g fill="#ffffff" font-family="Arial, sans-serif" font-size="28" text-anchor="middle">
      <text x="170" y="34">★</text><text x="117" y="63">★</text>
      <text x="678" y="34">★</text><text x="732" y="63">★</text>
      <text x="77" y="104">★</text><text x="778" y="104">★</text>
      <rect x="226" y="238" width="44" height="4"/>
      <text x="308" y="250">★</text>
      <rect x="346" y="238" width="44" height="4"/>
      <text x="428" y="250">★</text>
      <rect x="468" y="238" width="44" height="4"/>
      <text x="549" y="250">★</text>
      <rect x="588" y="238" width="44" height="4"/>
    </g>
  </svg>
  <span class="event-tournament">★ TOURNAMENT ★</span>
  <div class="event-year">2019</div>

  <svg class="connectors" width="848" height="200" viewBox="0 0 848 200" aria-hidden="true">
    <g stroke="#8dbb4a" stroke-width="4" fill="#8dbb4a">
      <line x1="0" y1="16" x2="848" y2="16"/>
      <line x1="51" y1="16" x2="51" y2="166"/>
      <line x1="51" y1="86" x2="108" y2="86"/>
      <line x1="51" y1="166" x2="108" y2="166"/>
      <line x1="517" y1="16" x2="517" y2="64"/>
      <line x1="710" y1="16" x2="710" y2="64"/>
      <circle cx="51" cy="16" r="7" stroke="none"/>
      <circle cx="517" cy="16" r="7" stroke="none"/>
      <circle cx="710" cy="16" r="7" stroke="none"/>
      <circle cx="517" cy="64" r="7" stroke="none"/>
      <circle cx="710" cy="64" r="7" stroke="none"/>
      <circle cx="51" cy="86" r="7" stroke="none"/>
      <circle cx="51" cy="166" r="7" stroke="none"/>
      <circle cx="108" cy="86" r="27" stroke="none"/>
      <circle cx="108" cy="166" r="27" stroke="none"/>
    </g>
    <path d="M108 70 a11 11 0 0 1 11 11 c0 9 -11 21 -11 21 s-11 -12 -11 -21 a11 11 0 0 1 11 -11z" fill="#ffffff"/>
    <circle cx="108" cy="81" r="4.5" fill="#8dbb4a"/>
    <rect x="98" y="153" width="20" height="26" rx="2" fill="#ffffff"/>
    <g stroke="#8dbb4a" stroke-width="2"><line x1="102" y1="160" x2="114" y2="160"/><line x1="102" y1="166" x2="114" y2="166"/><line x1="102" y1="172" x2="110" y2="172"/></g>
  </svg>

  <p class="detail detail-location">Brindle Oaks Links</p>
  <p class="detail detail-price"><span class="price">$175</span> individual<br><span class="price">$700</span> foursome</p>

  <div class="date-box">May<span class="date-day">15</span>, 2019</div>

  <div class="divider"></div>
  <p class="sponsor-line">Sponsorships starting at <span class="price">$250</span></p>
  <p class="benefit-line">Benefiting O-RamVT and the Pathway Builders Learning Grant Fund</p>
</main>
</body>
</html>
```